Scientific Web Site for TALQUIRE

Professional Scientific / Service orientated web site, motto, new logos attached for viewing.

"We measure so the Business Owner can Manage" their environments.
Site needs to be be mobile friendly.

We provide a service to electronically measure cleanliness of any surface and a value added disinfecting fogging surface.

Reports showing locations, trending, tracking and randomized test plans ongoing audits will be made available..

NOTE: Although image of Corona Virus is current we don't wont it plastered through the web site, their is more than the current virus.

Home Page - Professional Scientific / Service Looking
About
Our Approach
Services
Residential
Commercial
Transportation
Gyms
Educational & Daycare
Real Estate - Open for inspections, End of Lease etc

Contact
Mobile #
Email
Form to leave their details

Links to social media, Facebook, Instagram
Reference Sites: Ranked in preference
www.belunorm.com.au
https://www.vandrelhomecare.co.uk/
https://www.zelmarup.com/
https://www.ortivane.com.au/specialist-surface-disinfection/
https://www.plakorniv.com/design/48102937
https://www.plakorniv.com/design/59730418
https://www.plakorniv.com/design/41867205

Target Market(s)

Commercial and professional Services

Font styles to use
Sans Serif

Requirements
Must have
• Wix Website
Clean fresh look with appropriate imaging
Web site is a company advertising that will hold static information and we will market through social media.
Nice to have
• Scientific look and feel
Should not have
• Prominent Corona Virus images or references

```html
<!DOCTYPE html>
<html lang="en">
<head>
<meta charset="utf-8">
<title>Talquire — Disinfectant Fogging Services</title>
<link href="https://fonts.googleapis.com/css2?family=Poppins:wght@300;400;500;600;700;800&family=Roboto+Condensed:wght@400;500&display=swap" rel="stylesheet">
<style>
:root{
  --orange:#fe6a00;
  --black:#0c0c0c;
  --dark:#1e1e1e;
  --ink:#111;
  --muted:#8a8a8a;
  --line:#bdbdbd;
  --white:#fff;
  --light:#f3f3f3;
}
*{margin:0;padding:0;box-sizing:border-box}
html,body{width:1200px;height:3398px;overflow:hidden}
body{position:relative;font-family:'Poppins',sans-serif;color:var(--ink);background:var(--white)}
.abs{position:absolute}
.cond{font-family:'Roboto Condensed',sans-serif}

/* top bar */
.topbar{left:0;top:0;width:1200px;height:37px;background:var(--black)}
.topbar .call{left:720px;top:0;height:37px;width:206px;border-left:1px solid #333;display:flex;align-items:center;gap:12px;padding-left:18px;color:#fff;font-size:12px}
.topbar .soc{top:0;width:38px;height:37px;border-left:1px solid #333;display:flex;align-items:center;justify-content:center}
.topbar .soc span{width:9px;height:9px;background:var(--orange)}

/* header */
.header{left:0;top:37px;width:1200px;height:75px;background:var(--white)}
.logo{display:flex;align-items:center;gap:8px;font-weight:600;letter-spacing:3px;color:var(--ink)}
.logo .dot{width:12px;height:12px;background:var(--orange)}
.header .logo{left:161px;top:22px;font-size:24px}
.nav{left:534px;top:0;height:75px;display:flex;gap:26px;align-items:center;font-size:12px;color:#888}
.nav a{color:inherit;text-decoration:none;position:relative;height:75px;display:flex;align-items:center}
.nav a.active{color:var(--orange)}
.nav a.active:after{content:"";position:absolute;left:0;right:0;bottom:0;height:3px;background:var(--orange)}

/* hero */
.hero{left:0;top:112px;width:1200px;height:638px;background:radial-gradient(ellipse at 70% 30%,#6b5a45 0%,#3a332c 45%,#1c1a18 100%)}
.hero .t1{left:0;width:1200px;top:278px;text-align:center;font-size:52px;font-weight:800;color:var(--orange);line-height:1}
.hero .t2{left:0;width:1200px;top:340px;text-align:center;font-size:54px;font-weight:800;color:#fff;line-height:1;text-shadow:0 2px 6px rgba(0,0,0,.4)}
.hero .sub{left:0;width:1200px;top:408px;text-align:center;font-size:23px;color:#fff}
.btn{background:var(--orange);color:#fff;display:flex;align-items:center;justify-content:center;font-family:'Roboto Condensed',sans-serif;font-size:15px}
.hero .btn{left:539px;top:461px;width:120px;height:44px}
.arrow{width:37px;height:37px;display:flex;align-items:center;justify-content:center}
.orangeline{left:0;top:747px;width:1200px;height:3px;background:var(--orange)}

/* hexagons */
.hex{width:138px;height:121px;clip-path:polygon(25% 0,75% 0,100% 50%,75% 100%,25% 100%,0 50%);background:var(--orange);color:#fff;display:flex;flex-direction:column;align-items:center;justify-content:center;gap:8px;font-family:'Roboto Condensed',sans-serif;font-size:13px}
.hex.black{background:var(--black)}

/* welcome */
.welcome{left:0;top:750px;width:1200px;height:577px;background:linear-gradient(180deg,#f6f6f6,#ececec)}
.sectitle{left:0;width:1200px;text-align:center;font-size:35px;font-weight:600;display:flex;align-items:center;justify-content:center;gap:16px}
.sectitle:before,.sectitle:after{content:"";width:75px;height:1px;background:var(--line)}
.sectitle.light{color:#fff}
.sectitle.light:before,.sectitle.light:after{background:#777}
.about-frame1{left:161px;top:975px;width:112px;height:112px;border-left:14px solid var(--orange);border-top:14px solid var(--orange)}
.about-frame2{left:460px;top:1148px;width:114px;height:112px;border-right:6px solid var(--orange);border-bottom:6px solid var(--orange)}
.about-photo{left:175px;top:989px;width:391px;height:262px;background:linear-gradient(135deg,#e8ecef,#c8ccd0 60%,#8b8f94)}
.about h3{font-size:19px;font-weight:400;margin-bottom:14px}
.about p{font-size:10.5px;line-height:18.5px;color:var(--muted);margin-bottom:10px}
.about .btn{width:120px;height:44px;margin-top:22px}

/* services */
.services{left:0;top:1327px;width:1200px;height:592px;background:linear-gradient(180deg,#262626,#1a1a1a)}
.card{background:#fff;border-radius:3px}
.svc .photo{position:absolute;left:8px;top:7px;right:8px;height:180px}
.svc .icon{position:absolute;left:105px;top:162px;width:64px;height:56px;clip-path:polygon(25% 0,75% 0,100% 50%,75% 100%,25% 100%,0 50%);background:var(--orange)}
.svc h4{position:absolute;left:0;right:0;top:240px;text-align:center;font-family:'Roboto Condensed',sans-serif;font-size:19px;font-weight:400}
.svc p{position:absolute;left:20px;right:20px;top:278px;text-align:center;font-size:10.5px;line-height:19px;color:#666}

/* feedback */
.feedback-text{left:305px;top:2102px;width:590px;text-align:center;font-size:10.5px;line-height:19.5px;color:#999}
.client{left:0;width:1200px;top:2203px;text-align:center;font-size:14px;color:#333}
.dots{left:575px;top:2257px;display:flex;gap:8px}
.dots span{width:11px;height:11px;border:1px solid #888}
.dots span.on{border-color:var(--orange);background:radial-gradient(var(--orange) 45%,#fff 50%)}

/* blog */
.blogbg{left:0;top:2279px;width:1200px;height:630px;background:linear-gradient(180deg,#3a3a3a,#1f1f1f)}
.blog .photo{position:absolute;left:8px;top:8px;right:8px;height:163px}
.blog .date{position:absolute;left:14px;top:161px;width:104px;height:26px;background:var(--orange);color:#fff;font-family:'Roboto Condensed',sans-serif;font-size:13px;display:flex;align-items:center;justify-content:center}
.blog h5{position:absolute;left:17px;top:207px;font-size:14px;font-weight:400}
.blog p{position:absolute;left:17px;right:14px;top:240px;font-size:10.5px;line-height:19px;color:#999}
.blog a{position:absolute;left:17px;top:318px;font-size:10px;color:var(--orange)}

/* footer */
.footer .logo{left:0;width:1200px;top:3010px;justify-content:center;font-size:30px}
.footer-text{left:0;width:1200px;top:3072px;text-align:center;font-size:10.5px;line-height:19px;color:#999}
.subscribe{left:393px;top:3135px;width:413px;height:43px;display:flex}
.subscribe .field{flex:1;border:1px solid #ccc;font-size:11px;color:#666;display:flex;align-items:center;padding-left:12px}
.subscribe .btn{width:120px;height:43px;font-size:15px}
.footnav{left:0;width:1200px;top:3204px;display:flex;justify-content:center;gap:12px;font-size:12.5px;color:#555}
.footsoc{left:542px;top:3244px;display:flex;gap:9px}
.footsoc span{width:32px;height:32px;background:#4a6fb5;display:flex;align-items:center;justify-content:center}
.footsoc span:after{content:"";width:8px;height:8px;background:#fff}
.footsoc span.b{background:#3aa0e0}
.footsoc span.c{background:#2d74b0}
.copy{left:0;top:3338px;width:1200px;height:60px;background:var(--black);color:#aaa;font-size:11px;display:flex;align-items:center;justify-content:center}
</style>
</head>
<body>

<div class="abs topbar">
  <div class="abs call">
    <svg width="16" height="16" viewBox="0 0 24 24"><path d="M6 3l3 4-2 2a12 12 0 0 0 8 8l2-2 4 3-2 4C11 22 2 13 2 5z" fill="#fe6a00"/></svg>
    Call Us &nbsp;: &nbsp;123.456.7890
  </div>
  <div class="abs soc" style="left:926px"><span></span></div>
  <div class="abs soc" style="left:964px"><span></span></div>
  <div class="abs soc" style="left:1002px;border-right:1px solid #333"><span></span></div>
</div>

<header class="abs header">
  <div class="abs logo"><span class="dot"></span>TALQUIRE</div>
  <nav class="abs nav">
    <a class="active">Home</a><a>About</a><a>Services</a><a>Our Approach</a><a>Reviews</a><a>Blog</a><a>Contact</a>
    <svg width="15" height="15" viewBox="0 0 16 16"><circle cx="6.5" cy="6.5" r="5" stroke="#222" stroke-width="1.6" fill="none"/><path d="M10.5 10.5L15 15" stroke="#222" stroke-width="1.6"/></svg>
  </nav>
</header>

<section class="abs hero" role="img" aria-label="Technicians in protective suits fogging a restaurant interior"></section>
<div class="abs hero" style="background:none">
  <div class="abs t1" style="top:166px">DISINFECTANT</div>
  <div class="abs t2" style="top:228px">FOGGING SERVICES</div>
  <div class="abs sub" style="top:296px">We measure so the Business Owner can Manage</div>
  <div class="abs btn" style="top:349px">LEARN MORE</div>
  <div class="abs arrow" style="left:142px;top:270px;background:var(--orange)"><svg width="10" height="16"><path d="M8 1L2 8l6 7" stroke="#fff" fill="none" stroke-width="1.5"/></svg></div>
  <div class="abs arrow" style="left:1021px;top:270px;background:#bdbdbd"><svg width="10" height="16"><path d="M2 1l6 7-6 7" stroke="#fff" fill="none" stroke-width="1.5"/></svg></div>
</div>

<section class="abs welcome" role="img" aria-label="Faint background of a disinfection technician at work"></section>
<div class="abs orangeline"></div>

<div class="abs hex" style="left:193px;top:689px"><svg width="40" height="40" viewBox="0 0 40 40" fill="none" stroke="#fff" stroke-width="2"><circle cx="20" cy="18" r="10"/><path d="M14 34h12M20 28v6"/></svg>Most Effective</div>
<div class="abs hex" style="left:362px;top:689px"><svg width="40" height="40" viewBox="0 0 40 40" fill="none" stroke="#fff" stroke-width="2"><circle cx="22" cy="23" r="12"/><path d="M22 23l5-6M18 6h8M22 6v5"/></svg>Fast</div>
<div class="abs hex black" style="left:531px;top:689px"><svg width="40" height="40" viewBox="0 0 40 40" fill="none" stroke="#fff" stroke-width="2"><circle cx="20" cy="18" r="10"/><path d="M14 34h12M20 28v6"/></svg>Environmental</div>
<div class="abs hex" style="left:700px;top:689px"><svg width="40" height="40" viewBox="0 0 40 40" fill="none" stroke="#fff" stroke-width="2"><path d="M8 20c0 8 5 14 12 14s12-6 12-14M20 6v20M14 12l6 6 6-6"/></svg>Safe</div>
<div class="abs hex" style="left:869px;top:689px"><svg width="40" height="40" viewBox="0 0 40 40" fill="none" stroke="#fff" stroke-width="2"><circle cx="20" cy="25" r="10"/><path d="M16 15V9h8v6M24 9h6"/></svg>Smells Great</div>

<h2 class="abs sectitle" style="top:862px">Welcome To Talquire</h2>

<div class="abs about-frame1"></div>
<div class="abs about-frame2"></div>
<div class="abs about-photo" role="img" aria-label="Technician with backpack sprayer treating a wall beside a client"></div>
<div class="abs about" style="left:646px;top:988px;width:385px">
  <h3>About Environment Disinfected</h3>
  <p>Lorem ipsum dolor sit amet, consectetur adipiscing elit, sed do eiusmod tempor incididunt ut labore et dolore magna aliqua. Ut enim ad minim veniam, quis nostrud exercitation ullamco laboris nisi ut aliquip ex ea commodo consequat. Duis aute irure dolor in reprehenderit in voluptate velit esse cillum dolore eu fugiat nulla pariatur.</p>
  <p>Lorem ipsum dolor sit amet, consectetur adipiscing elit, sed do eiusmod tempor incididunt ut labore et dolore magna aliqua. Ut enim ad minim veniam, quis nostrud exercitation ullamco.</p>
  <div class="btn">LEARN MORE</div>
</div>

<section class="abs services" role="img" aria-label="Dark background of a technician working in a facility"></section>
<h2 class="abs sectitle light" style="top:1380px">Our Services</h2>

<div class="abs card svc" style="left:161px;top:1455px;width:270px;height:336px">
  <div class="photo" role="img" aria-label="Technician fogging a residential kitchen" style="background:linear-gradient(135deg,#d9d4cc,#9a9288)"></div>
  <div class="icon"></div><h4>Residential</h4>
  <p>Lorem ipsum dolor sit amet, consectetur incididunt magna aliqua.</p>
</div>
<div class="abs card svc" style="left:465px;top:1455px;width:270px;height:336px">
  <div class="photo" role="img" aria-label="Technician fogging an office space" style="background:linear-gradient(135deg,#8a8a86,#3e3e3c)"></div>
  <div class="icon"></div><h4>Commercial</h4>
  <p>Lorem ipsum dolor sit amet, consectetur incididunt magna aliqua.</p>
</div>
<div class="abs card svc" style="left:769px;top:1455px;width:270px;height:336px">
  <div class="photo" role="img" aria-label="Crew disinfecting a train carriage" style="background:linear-gradient(135deg,#b9c7d4,#2f6ea3)"></div>
  <div class="icon"></div><h4>Transportation</h4>
  <p>Lorem ipsum dolor sit amet, consectetur incididunt magna aliqua.</p>
</div>
<div class="abs arrow" style="left:1061px;top:1609px;width:29px;height:29px;background:#777"><svg width="8" height="14"><path d="M1 1l6 6-6 6" stroke="#fff" fill="none" stroke-width="1.4"/></svg></div>

<svg class="abs" style="left:0;top:1859px" width="1200" height="60"><polygon points="0,60 600,0 1200,60" fill="#fff"/></svg>

<h2 class="abs sectitle" style="top:1926px">Client's Feedback</h2>
<svg class="abs" style="left:552px;top:2000px" width="92" height="80" viewBox="0 0 92 80">
  <polygon points="23,2 69,2 90,40 69,78 23,78 2,40" fill="none" stroke="#fe6a00" stroke-width="3"/>
  <polygon points="27,9 65,9 82,40 65,71 27,71 10,40" fill="#c9ccd1"/>
  <circle cx="80" cy="58" r="11" fill="#fe6a00"/>
</svg>
<svg class="abs" style="left:265px;top:2118px" width="14" height="36"><path d="M12 1L2 18l10 17" stroke="#333" fill="none"/></svg>
<svg class="abs" style="left:921px;top:2118px" width="14" height="36"><path d="M2 1l10 17-10 17" stroke="#fe6a00" fill="none"/></svg>
<p class="abs feedback-text">Lorem ipsum dolor sit amet, consectetur adipiscing elit, sed do eiusmod tempor incididunt ut labore et dolore magna aliqua. Ut enim ad minim veniam, quis nostrud exercitation ullamco laboris nisi ut aliquip ex ea commodo consequat. Duis aute irure dolor in reprehenderit in voluptate velit esse cillum dolore eu fugiat nulla pariatur. Excepteur sint occaecat cupidatat non proident.</p>
<div class="abs client cond">— &nbsp;Client's Name</div>
<div class="abs dots"><span></span><span class="on"></span><span></span></div>

<section class="abs blogbg" role="img" aria-label="Dark background of a technician disinfecting a room"></section>
<svg class="abs" style="left:0;top:2278px" width="1200" height="62"><polygon points="0,0 1200,0 1200,1 600,61 0,1" fill="#fff"/></svg>
<h2 class="abs sectitle light" style="top:2392px">Recent Blog</h2>

<div class="abs card blog" style="left:161px;top:2474px;width:270px;height:352px">
  <div class="photo" role="img" aria-label="Technician fogging a classroom" style="background:linear-gradient(135deg,#c9b27a,#6c6a62)"></div>
  <div class="date">15 Sep 2020</div>
  <h5>Lorem ipsum dolor</h5>
  <p>Lorem ipsum dolor sit amet, consect adipisc ing elit, sed do eiusmod tempor incididunt ut labore et dolore magna aliqua.</p>
  <a>LEARN MORE</a>
</div>
<div class="abs card blog" style="left:465px;top:2474px;width:270px;height:352px">
  <div class="photo" role="img" aria-label="Worker in protective gear wiping a window" style="background:linear-gradient(135deg,#eef3f6,#b5cbd9)"></div>
  <div class="date">15 Sep 2020</div>
  <h5>Lorem ipsum dolor</h5>
  <p>Lorem ipsum dolor sit amet, consect adipisc ing elit, sed do eiusmod tempor incididunt ut labore et dolore magna aliqua.</p>
  <a>LEARN MORE</a>
</div>
<div class="abs card blog" style="left:769px;top:2474px;width:270px;height:352px">
  <div class="photo" role="img" aria-label="Staff cleaning gym equipment" style="background:linear-gradient(135deg,#9a938b,#2c2c2c)"></div>
  <div class="date">15 Sep 2020</div>
  <h5>Lorem ipsum dolor</h5>
  <p>Lorem ipsum dolor sit amet, consect adipisc ing elit, sed do eiusmod tempor incididunt ut labore et dolore magna aliqua.</p>
  <a>LEARN MORE</a>
</div>

<footer class="footer">
  <div class="abs logo"><span class="dot"></span>TALQUIRE</div>
  <p class="abs footer-text">Lorem ipsum dolor sit amet, consectetur adipiscing elit, sed do eiusmod<br>tempor &nbsp;Excepteur sint occaecat cupidatat non proident.</p>
  <div class="abs subscribe"><div class="field">Enter Email....</div><div class="btn">SUBCRIBE NOW</div></div>
  <div class="abs footnav"><span>Home</span>|<span>About</span>|<span>Services</span>|<span>Our Approach</span>|<span>Reviews</span>|<span>&nbsp;Blog&nbsp;</span>|<span>&nbsp;Contact</span></div>
  <div class="abs footsoc"><span></span><span class="b"></span><span class="c"></span></div>
  <div class="abs copy">Copyright © TALQUIRE – 2020 . All Right Reserved.</div>
</footer>

</body>
</html>
```